TRELUDAX.live*

I am needing a web site built for the main purpose of uploading podcasts
(MP3 files) to be viewed by large audiences of 1000+ site visitors on a regular basis. I have created a rough draft of how I want the site to look.

i have created a rough draft of the home page - the LOGO for this site is a spectacular lightening bolt which appears on my home page sample... the file for this image I purchased is too large to download to your site. I will supply on reuquest.

There will be 5 pages; HOME ABOUT RESOURCES DEVOTIONALS GLENN.
I have all the content prepared for each of the above pages.

Target Market(s)

All people groups seeking positive and encouraging words, life lessons and testimonies of faith.

Coding

Coded - Design and coding required

Number of Pages Required

1 page

Colors
3176b5

Requirements
Must have
• The design and layout provided - my sample

Black backgrounds as shown on my sample

```html
<!DOCTYPE html>
<html lang="en">
<head>
<meta charset="utf-8">
<title>TRELUDAX.live</title>
<link href="https://fonts.googleapis.com/css2?family=Playfair+Display:wght@900&family=Work+Sans:wght@400;500&display=swap" rel="stylesheet">
<style>
  :root{
    --black:#000;
    --charcoal:#221f20;
    --mist:#f1f5f8;
    --blue:#3176b5;
    --red:#e3262f;
    --white:#fff;
    --grey:#c7c7c7;
    --line:#2c2c2c;
  }
  *{margin:0;padding:0;box-sizing:border-box}
  html,body{width:1200px;height:909px;overflow:hidden;background:var(--black)}
  body{position:relative;font-family:"Work Sans",sans-serif}

  .site-header{position:absolute;left:0;top:0;width:1200px;height:80px;background:var(--black);border-bottom:2px solid var(--line)}
  .nav-link{position:absolute;top:37px;font-size:17px;font-weight:500;color:var(--red);text-decoration:none;letter-spacing:.2px}
  .nav-link.is-active{color:var(--blue)}
  .nav-underline{position:absolute;left:88px;top:77px;width:64px;height:2px;background:var(--blue)}
  .nav-underline::after{content:"";position:absolute;left:28px;top:-4px;border:4px solid transparent;border-bottom-color:var(--blue);border-top:0}
  .brand{position:absolute;left:0;width:1200px;top:18px;text-align:center;font-family:"Playfair Display",serif;font-weight:900;font-size:36px;color:var(--white);letter-spacing:1px}

  .hero{position:absolute;left:0;top:80px;width:1200px;height:480px;background:var(--black);overflow:hidden}
  .hero-art{position:absolute;left:0;top:0}
  .hero-mark{position:absolute;left:1002px;top:152px;width:76px;height:76px;border:3px solid var(--red);border-radius:50%}
  .podcast-title{position:absolute;left:880px;width:320px;top:262px;text-align:center;font-family:"Playfair Display",serif;font-weight:900;font-size:30px;line-height:38px;color:var(--white);letter-spacing:1.5px}

  .episodes-band{position:absolute;left:0;top:560px;width:1200px;height:160px;background:var(--charcoal)}
  .episodes-floor{position:absolute;left:0;top:720px;width:1200px;height:140px;background:var(--mist)}
  .episodes{position:absolute;left:32px;top:592px;width:1136px;height:240px;display:flex}
  .episode{flex:1;background:var(--black);border-left:1px solid var(--line);position:relative;text-align:center;color:var(--white)}
  .episode:first-child{border-left:0}
  .episode.is-active{background:var(--blue);border-left-color:var(--blue)}
  .episode-mark{position:absolute;left:88px;top:50px;width:52px;height:52px;border:3px solid var(--red);border-radius:50%}
  .episode.is-active .episode-mark{border-color:var(--white)}
  .episode-date{position:absolute;left:0;right:0;top:126px;font-size:13px;color:var(--blue)}
  .episode.is-active .episode-date{color:var(--white)}
  .episode-title{position:absolute;left:0;right:0;top:144px;font-size:16px;font-weight:500;line-height:24px}
  .episode-bar{position:absolute;left:54px;bottom:0;width:120px;height:4px;background:var(--blue)}
  .episode.is-active .episode-bar{display:none}

  .site-footer{position:absolute;left:0;top:860px;width:1200px;height:49px;background:var(--charcoal);color:var(--grey);font-size:13px;text-align:center;line-height:49px}
</style>
</head>
<body>
<header class="site-header">
  <a class="nav-link is-active" style="left:98px">HOME</a>
  <span class="nav-underline"></span>
  <a class="nav-link" style="left:188px">ABOUT</a>
  <a class="nav-link" style="left:284px">GLENN</a>
  <div class="brand">TRELUDAX.live</div>
  <a class="nav-link" style="left:869px">RESOURCES</a>
  <a class="nav-link" style="left:1006px">DEVOTIONALS</a>
</header>

<section class="hero">
  <svg class="hero-art" width="1200" height="480" viewBox="0 0 1200 480">
    <defs>
      <radialGradient id="bolt-glow" cx="50%" cy="50%" r="50%">
        <stop offset="0" stop-color="#2fd2ff"/>
        <stop offset=".35" stop-color="#0a3fc9" stop-opacity=".8"/>
        <stop offset="1" stop-color="#000" stop-opacity="0"/>
      </radialGradient>
      <linearGradient id="photo-tone" x1="0" y1="0" x2="0" y2="1">
        <stop offset="0" stop-color="#2a2a2c"/>
        <stop offset=".6" stop-color="#1a1a1c"/>
        <stop offset="1" stop-color="#5a3a1e"/>
      </linearGradient>
    </defs>
    <ellipse role="img" aria-label="Glowing blue lightning bolt artwork" cx="160" cy="250" rx="150" ry="190" fill="url(#bolt-glow)"/>
    <polygon role="img" aria-label="Photo of the host seated beside a motorcycle" points="432,0 928,0 768,480 272,480" fill="url(#photo-tone)"/>
    <polygon points="398,140 411,140 292,420 280,420" fill="var(--red)"/>
    <polygon points="908,140 920,140 800,420 788,420" fill="var(--blue)"/>
  </svg>
  <span class="hero-mark" aria-hidden="true"></span>
  <h1 class="podcast-title">LIFE CHANGING<br>PODCASTS</h1>
</section>

<div class="episodes-band"></div>
<div class="episodes-floor"></div>
<section class="episodes">
  <article class="episode"><span class="episode-mark"></span><p class="episode-date">18-AUG-2020</p><h2 class="episode-title">Contrary popular belief,<br>Lorem Ipsum</h2><span class="episode-bar"></span></article>
  <article class="episode"><span class="episode-mark"></span><p class="episode-date">18-AUG-2020</p><h2 class="episode-title">Contrary popular belief,<br>Lorem Ipsum</h2><span class="episode-bar"></span></article>
  <article class="episode is-active"><span class="episode-mark"></span><p class="episode-date">18-AUG-2020</p><h2 class="episode-title">Contrary popular belief,<br>Lorem Ipsum</h2><span class="episode-bar"></span></article>
  <article class="episode"><span class="episode-mark"></span><p class="episode-date">18-AUG-2020</p><h2 class="episode-title">Contrary popular belief,<br>Lorem Ipsum</h2><span class="episode-bar"></span></article>
  <article class="episode"><span class="episode-mark"></span><p class="episode-date">18-AUG-2020</p><h2 class="episode-title">Contrary popular belief,<br>Lorem Ipsum</h2><span class="episode-bar"></span></article>
</section>

<footer class="site-footer">© 2020 Treludax. All Right Reserved</footer>
</body>
</html>
```